Update, redesign www.quorvane.net. Put it on Sitecraft and migrate to new host site

My current website is www.quorvane.net. The text content is ok but the site look and feel is several years old and does not project a sense of innovation. I am looking for a more modern exciting look. It needs to be built on word press and I need help in in putting it with a new hosting service.

Target Market(s)

Established organizations

Industry/Entity Type

Business Consultant

Number of Pages Required

1 page

Font styles to use
Sans Serif

Colors

Designer to choose colors to be used in the design.

Requirements
Must have
• Simple. Easy to read and navigate
Nice to have
• Innovation, creativity especially the leadership of innovation. Reading the current text on www.quorvane.net should help you with ideas
Should not have
• Difficulty in me managing or adding content after it is built

```html
<!DOCTYPE html>
<html lang="en">
<head>
<meta charset="utf-8">
<title>quorvane — Innovation at work</title>
<link rel="stylesheet" href="https://fonts.googleapis.com/css2?family=Arimo:wght@400;700&family=PT+Sans:wght@400;700&display=swap">
<style>
:root{
  --brand:#ed1a2f;
  --brand-dark:#9c1320;
  --ink:#333333;
  --text:#747474;
  --line:#e3e3e3;
  --tab-bg:#ebebeb;
  --footer:#2d2d2d;
  --footer-text:#8c8c8c;
  --white:#ffffff;
}
*{box-sizing:border-box;margin:0;padding:0}
html,body{width:901px;height:1200px;overflow:hidden;background:var(--white)}
body{position:relative;font-family:"PT Sans",sans-serif;color:var(--text)}
.abs{position:absolute}
a{color:inherit;text-decoration:none}

/* header */
.site-header{left:0;top:0;width:901px;height:56px;background:var(--white)}
.logo{left:106px;top:11px;font:700 26px/1 "PT Sans",sans-serif;color:var(--brand);letter-spacing:0.3px}
.main-nav{top:23px;left:0;width:901px;font:400 8.2px/1 Arimo,sans-serif;color:var(--ink)}
.main-nav a{position:absolute;white-space:nowrap}
.main-nav .current{color:var(--brand)}
.nav-marker{left:482px;top:0;width:24px;height:2px;background:var(--brand)}

/* hero */
.hero{left:0;top:56px;width:901px;height:406px;background:var(--brand)}
.hero h1{left:150px;top:140px;font:400 44px/1 "PT Sans",sans-serif;color:var(--white);letter-spacing:0.2px}
.hero p{left:153px;top:199px;width:300px;font-size:8.4px;line-height:15px;color:var(--white)}
.hero .btn{left:153px;top:269px;width:117px;height:25px;background:var(--white);color:var(--brand);font-size:8.4px;line-height:25px;text-align:center}
.hero .ring{left:608px;top:117px;width:132px;height:132px;border:3px solid var(--white);border-radius:50%}
.slide-arrow{top:169px;width:19px;height:68px;background:var(--brand-dark)}
.slide-arrow svg{position:absolute;left:6px;top:29px}

/* services */
.service-img{top:496px;height:120px}
.service h2{position:absolute;top:631px;font:400 11.3px/1 Arimo,sans-serif;color:var(--ink)}
.service p{position:absolute;top:654px;width:212px;font-size:9.4px;line-height:17px}
.more{color:var(--brand)}

/* tabs */
.tabs{left:106px;top:781px;width:331px;height:169px;border:1px solid var(--line)}
.tab{position:absolute;top:0;height:28px;font:400 8.6px/28px Arimo,sans-serif;color:var(--ink);text-align:center;background:var(--tab-bg)}
.tab.active{background:var(--white);border-top:2px solid var(--brand);line-height:26px}
.tabs p{position:absolute;left:10px;top:35px;width:312px;font-size:9.4px;line-height:17px}
.tabs em{font-size:10.6px}

/* book */
.book-title{left:457px;top:792px;font:400 15px/1 Arimo,sans-serif;color:var(--ink)}
.book-cover{left:459px;top:821px;width:53px;height:78px;background:linear-gradient(180deg,#e3262f 0%,#c81e28 70%,#173d22 85%,#d42030 100%)}
.book-text{left:522px;top:819px;width:275px;font-size:10.6px;line-height:17px}
.book-cta{left:523px;top:908px;font-size:10.6px;color:var(--brand)}

/* clients */
.clients-title{left:0;width:901px;top:1013px;text-align:center;font:400 15px/1 Arimo,sans-serif;color:var(--ink)}
.client{top:1046px;width:99px;height:72px;border:1px solid var(--line);display:flex;align-items:center;justify-content:center;font:700 12px/1 "PT Sans",sans-serif;color:#a6a6a6;letter-spacing:0.5px}

/* footer */
.site-footer{left:0;top:1149px;width:901px;height:51px;background:var(--footer)}
.site-footer p{position:absolute;left:106px;top:21px;font-size:7px;color:var(--footer-text)}
.site-footer strong{font-weight:400;color:#d6d6d6}
.social{position:absolute;top:21px;width:9px;height:9px;border-radius:50%;background:#6f6f6f}
</style>
</head>
<body>

<header class="site-header abs">
  <div class="nav-marker abs"></div>
  <a class="logo abs" href="#">quorvane</a>
  <nav class="main-nav abs">
    <a class="current" style="left:481px">Home</a>
    <a style="left:523px">About</a>
    <a style="left:566px">Thought Leadership</a>
    <a style="left:655px">Services</a>
    <a style="left:705px">Blog</a>
    <a style="left:740px">Contact</a>
    <svg class="abs" style="left:788px;top:-1px" width="9" height="9" viewBox="0 0 10 10" aria-label="Search"><circle cx="4" cy="4" r="3" fill="none" stroke="#333" stroke-width="1.5"/><line x1="6.2" y1="6.2" x2="9" y2="9" stroke="#333" stroke-width="1.5"/></svg>
  </nav>
</header>

<section class="hero abs">
  <h1 class="abs">Innovation at work</h1>
  <p class="abs">With over 30 years of combined experience in innovating in the real world<br>we know what works and what doesn’t. We are pragmatists who quickly<br>and efficiently accelerate our client’s innovation initiatives from frategic<br>intent through ideation and implementation to value creation.</p>
  <a class="btn abs" href="#">Learn about Consulting</a>
  <div class="ring abs"></div>
  <div class="slide-arrow abs" style="left:0"><svg width="7" height="10" viewBox="0 0 7 10"><polyline points="5,1 1,5 5,9" fill="none" stroke="#fff" stroke-width="1.4"/></svg></div>
  <div class="slide-arrow abs" style="left:882px"><svg width="7" height="10" viewBox="0 0 7 10"><polyline points="2,1 6,5 2,9" fill="none" stroke="#fff" stroke-width="1.4"/></svg></div>
</section>

<div class="service-img abs" style="left:106px;width:211px;background:linear-gradient(135deg,#eef0f3,#c9ccd2 60%,#7d8aa3)" role="img" aria-label="Consultant and client reviewing work together at a laptop"></div>
<div class="service-img abs" style="left:345px;width:211px;background:linear-gradient(135deg,#d9dde3,#7d8594 55%,#2f3644)" role="img" aria-label="Executives seated in a row at an education session"></div>
<div class="service-img abs" style="left:584px;width:211px;background:linear-gradient(135deg,#3a5274,#8b8f99 50%,#d7b6a4)" role="img" aria-label="Speaker addressing a seated audience"></div>

<div class="service abs" style="left:106px;top:0">
  <h2 style="left:0">Consulting</h2>
  <p style="left:0">We consult with both private and public sector organizations. Our goal is to help our clients utilize innovation as a tool to enhance organizational performance and to gain competitive advantage. <span class="more">Read more &gt;</span></p>
</div>
<div class="service abs" style="left:345px;top:0">
  <h2 style="left:0">Executive Education</h2>
  <p style="left:0">The quorvane team are all seasoned executive educaton professionals. We offer a number of executive education programs form quick start ideation though to strategic business development courses utilize. <span class="more">Read More &gt;</span></p>
</div>
<div class="service abs" style="left:583px;top:0">
  <h2 style="left:0">Speaking</h2>
  <p style="left:0">We stay on top of our field by actively engaging in research, networking with other top people in the field of innovation,  and writing about what we and our clients have learned. While our work iis firmly grounded in theory. <span class="more">Read more &gt;</span></p>
</div>

<div class="tabs abs">
  <div class="tab active" style="left:0;width:110px">About quorvane</div>
  <div class="tab" style="left:110px;width:109px">Testimonials</div>
  <div class="tab" style="left:219px;width:111px">Team</div>
  <p><em>Idea Dojo</em> - reveals 7 secret principles that can help any innovator overcome the roadblocks and blockheads that they will inevitably meet on the path to creativity. And these principles do not presuppose an innovation friendly culture. In fact, the profiles in this book will introduce you to innovators who have succeeded even when their organizations’ culture was either not particularly friendly to new ideas or even downright hostile.</p>
</div>

<h2 class="book-title abs">Order Idea Dojo</h2>
<div class="book-cover abs" role="img" aria-label="Cover of the book Idea Dojo by Corin Ashdale"></div>
<p class="book-text abs">quorvane works with a broad range of national and global clients to ultilize “Innovation at Work” to improve business results. We help individuals and organizations through the entire value chain of innovation from idea generation, implementation and value creation.</p>
<a class="book-cta abs" href="#">Order Now &gt;</a>

<h2 class="clients-title abs">Clients</h2>
<div class="client abs" style="left:111px">NORVIK</div>
<div class="client abs" style="left:227px">HALBROOK</div>
<div class="client abs" style="left:343px">CASTELA</div>
<div class="client abs" style="left:459px;font-size:10px">ARDENT HARBOR</div>
<div class="client abs" style="left:575px">VELTRANE</div>
<div class="client abs" style="left:691px">LUMORA</div>

<footer class="site-footer abs">
  <p>© Copyright 2019 Brightfold Publishing. All rights reserved.   |   Powered by <strong>Sitecraft</strong></p>
  <span class="social" style="left:689px"></span>
  <span class="social" style="left:713px"></span>
  <span class="social" style="left:737px"></span>
  <span class="social" style="left:760px"></span>
  <span class="social" style="left:784px"></span>
</footer>

</body>
</html>
```